Convert MS Word FIle into Magazine with a new Cover Design (Indesign)

Essentially, I need help to transform a simple MS Word document into a magazine. We are an alternative health supplier (Morvy flower remedies) looking to appeal to target market of women aged 25-45, who are interested in holistic healing/nwaw age/natural remedies. The magazine should have art nouveau or art deco touches, eluding to when Morvy flower essences were first discovered. I have some pictures in the document you must use, but feel free to add in relevant pictures and graphics that you see fit - such as flowers or pictures of essential oils etc.

Project is completed now! Thank you!

```html
<!DOCTYPE html>
<html lang="en">
<head>
<meta charset="utf-8">
<title>Introduction</title>
<link href="https://fonts.googleapis.com/css2?family=EB+Garamond:wght@400;700&display=swap" rel="stylesheet">
<style>
  :root {
    --page: #fcefe6;
    --band: #4f8e80;
    --band-text: #ffffff;
    --ink: #3a3230;
  }
  html, body {
    margin: 0;
    padding: 0;
    overflow: hidden;
  }
  body {
    width: 848px;
    height: 1200px;
    background: var(--page);
  }
  .page {
    position: relative;
    width: 848px;
    height: 1200px;
    box-sizing: border-box;
    padding: 149px 98px 0 107px;
    font-family: "EB Garamond", Georgia, serif;
    color: var(--ink);
  }
  .section-band {
    margin: 0 0 23px;
    height: 26px;
    background: var(--band);
    color: var(--band-text);
    text-align: center;
    font-weight: 700;
    font-size: 18px;
    letter-spacing: 0.6px;
    line-height: 26px;
  }
  .body-copy p {
    margin: 0 0 16px;
    font-size: 16.6px;
    line-height: 24.4px;
    text-align: justify;
    text-indent: 20px;
    hyphens: auto;
  }
  .float-spacer {
    float: left;
    width: 1px;
    height: 50px;
  }
  .brand-mark {
    float: left;
    clear: left;
    width: 283px;
    height: 240px;
    margin: 0 20px 0 0;
    display: flex;
    align-items: center;
    justify-content: center;
  }
  .brand-mark span {
    font-size: 26px;
    font-weight: 400;
    color: var(--ink);
    text-indent: 0;
    letter-spacing: 0.5px;
  }
</style>
</head>
<body>
  <main class="page">
    <h1 class="section-band">INTRODUCTION</h1>
    <div class="body-copy">
      <div class="float-spacer"></div>
      <div class="brand-mark" role="img" aria-label="Lumen &amp; Vale brand name"><span>Lumen &amp; Vale</span></div>
      <p>Morvy Flower Remedies were developed by Dr Edwin Morvy in the earlier part of the 20th century to directly address emotional imbalances. He believed that the root of all disease lies in the mind, and ultimately, deep in the vast depths of an individual’s soul. It is a belief that was also shared by the Greek philosopher Plato, and in traditional societies where medicine men play key central roles, providing physical and spiritual healing and as well as sage advice.</p>
      <p>Alternative therapies make no distinction between spirit and matter, unlike conventional medicine, where only alleviating the physical symptoms of disease matters. The wisdom of therapies such as Reiki, Ayurveda and Traditional Chinese Medicine, lie in the very fact that the substances vital to sustain life – such as blood, hormones and body fluids, are simply manifestations of the complex energetic field that flows in all of us. Therefore, in order to attain optimal health, it is crucial to keep this energy moving in a balanced state. Morvy Flower Remedies, which are a form of vibrational medicine, work directly on this live-giving internal energy system, helping to bring it back into a positive state when it is assailed by negativity. It is a holistic way of treating others, affording an appreciation of the individual.</p>
      <p>Aromatherapy works in a similar manner, influencing the mind and spirit through a physical medium that encapsulates the healing powers of nature.</p>
      <p>The primary aim of this book is to provide readers with the foundational tools to help them achieve healthy, fulfilling lives. By looking at the energetic aspects of each essential oil and Morvy Flower remedy, we will be able to distil their spiritual and psychological effects to intuitively tackle different emotional states and situations.</p>
      <p>Initially, we will look at Morvy Flower Remedies and Essential Oils in detail, specifically at its production methods and scientific studies supporting their use for emotional healing. In the subsequent chapters, we will explore Morvy Flower Remedies and their relevant essential oils in detail equipping you with the vital knowledge to heal yourself.</p>
    </div>
  </main>
</body>
</html>
```